Paleo Diet Book Cover Design

I need a cover designed for my book Stone Frame that will be sold on Brightleaf Reader and other sites. So the front, side and back will need to be designed. I have attached part of the book here so feel free to skim through the content and give it a quick read to get a feel for what the book is about. Stone Frame is about eating the diet of the caveman (paleolithic era-paleo) and a 12 week workout plan with a grocery shopping list and meal plans. It is for men and women ages 18+ who are interested in health and fitness and becoming healthier overall.
The graphics should be secondary, and it should add to the text, not distract from it. This is even more important because the size of the cover displayed on Brightleaf/Reader, when your book is first seen by a potential buyer, is so tiny. It's barely an inch high, and even smaller in width.
So the words have to be big, bold, benefit-rich and easy to read. That also means, don't mess with the fancy fonts. Clean, clear, crisp font is best. And, did I say BIG already?
Contrast the colors of the text and background, so its even easier to read. That means, dark text on light background or visa versa. Colors like darker reds, blues / teals and oranges.
Please read this: http://www.jacketforge.net/8-cover-design-secrets-publishers-use-to-manipulate-readers-into-buying-books/
The cover has to be bold and easy to read, it has to stick out, it has to draw the attention of your readers so that they zero in on my book, out of all the other books on the page. (Much like they would when viewing a classified ads site/page.)
The Title of the Book is Stone Frame, and the subtitle is "Transform Your Body For Life in 12 Weeks With Proven Workouts and Paleo Diet Based Nutrition" Perhaps “Transform Your Body For Life in 12 Weeks” could also be in a large font similar to the title with the rest of the subtitle following afterwards. You can try having the title be the smaller font with the subtitle being the larger font as well.
Then the authors name "Martin Oakes” incorporated into the design.
I am not sure what to use as the background type of design for the front of the book so feel free to be creative with that.
The size needs to be 1563 pixels on the shortest side and 2500 pixels on the longest side just for the front of the cover.

```html
<!DOCTYPE html>
<html lang="en">
<head>
<meta charset="utf-8">
<title>Stone Frame – Book Cover</title>
<link rel="stylesheet" href="https://fonts.googleapis.com/css2?family=Montserrat:ital,wght@0,700;0,800;0,900;1,700;1,800;1,900&display=swap">
<style>
  :root {
    --page-bg: #ffffff;
    --sky-top: #0d3f9e;
    --sky-mid: #1f6fd6;
    --sky-low: #3d8fe6;
    --orange-soft: rgba(246, 168, 30, 0);
    --orange-top: #f6a81e;
    --orange-low: #f5b43a;
    --title-yellow: #f7b51b;
    --title-white: #ffffff;
    --title-silver: #c9d3de;
    --ink: #141414;
    --author-band: #1a62c8;
  }

  * { margin: 0; padding: 0; box-sizing: border-box; }

  html, body {
    width: 1200px;
    height: 967px;
    overflow: hidden;
    background: var(--page-bg);
  }

  .stage {
    position: relative;
    width: 1200px;
    height: 967px;
  }

  .cover {
    position: absolute;
    left: 312px;
    top: 23px;
    width: 576px;
    height: 920px;
    overflow: hidden;
    background: linear-gradient(180deg, var(--sky-top) 0%, var(--sky-mid) 28%, var(--sky-low) 50%);
    font-family: "Montserrat", "Helvetica Neue", Arial, sans-serif;
  }

  .cover-photo {
    position: absolute;
    left: 0;
    top: 330px;
    width: 576px;
    height: 494px;
    background: linear-gradient(180deg, var(--orange-soft) 0%, var(--orange-top) 30%, var(--orange-low) 100%);
  }

  .title {
    position: absolute;
    left: 0;
    right: 0;
    top: 52px;
    text-align: center;
    line-height: 0.92;
  }

  .title-top {
    display: block;
    font-style: italic;
    font-weight: 900;
    font-size: 128px;
    letter-spacing: -2px;
    color: var(--title-yellow);
  }

  .title-bottom {
    display: block;
    font-weight: 800;
    font-size: 134px;
    letter-spacing: -2px;
    background: linear-gradient(180deg, var(--title-white) 55%, var(--title-silver) 100%);
    -webkit-background-clip: text;
    background-clip: text;
    color: transparent;
  }

  .subtitle {
    position: absolute;
    left: 240px;
    top: 612px;
    width: 330px;
    color: var(--ink);
    font-style: italic;
    line-height: 1;
  }

  .subtitle-small {
    display: block;
    font-weight: 700;
    font-size: 30px;
    letter-spacing: -0.5px;
    padding-left: 74px;
  }

  .subtitle-big {
    display: block;
    font-weight: 900;
    font-size: 48px;
    letter-spacing: -1px;
  }

  .subtitle .line-two { padding-left: 88px; margin-top: 8px; }
  .subtitle .line-four { margin-top: 2px; font-size: 56px; }

  .author-band {
    position: absolute;
    left: 0;
    bottom: 0;
    width: 576px;
    height: 96px;
    background: var(--author-band);
    display: flex;
    align-items: center;
    justify-content: flex-end;
    padding-right: 60px;
  }

  .author {
    font-style: italic;
    font-weight: 800;
    font-size: 32px;
    color: var(--title-white);
    letter-spacing: 0.5px;
  }
</style>
</head>
<body>
  <main class="stage">
    <article class="cover">
      <div class="cover-photo" role="img" aria-label="Photo of a slim waist wrapped in a yellow measuring tape"></div>

      <h1 class="title">
        <span class="title-top">STONE</span>
        <span class="title-bottom">FRAME</span>
      </h1>

      <p class="subtitle">
        <span class="subtitle-small">TRANSFORM</span>
        <span class="subtitle-big">YOUR BODY</span>
        <span class="subtitle-small line-two">FOR LIFE IN</span>
        <span class="subtitle-big line-four">12 WEEKS</span>
      </p>

      <footer class="author-band">
        <span class="author">MARTIN OAKES</span>
      </footer>
    </article>
  </main>
</body>
</html>
```